Business card design needed

Want the logo on a medium blue background and a nice funky design. I have my own gym and run one on one personal training and nutrition sessions. want it to look lively.
Updates

Please note I requested my logo on a blue background 

PLEASE NOTE: I already have a logo. It is attached to the order!!

Target Market(s)

over 55s

Industry/Entity Type

Nutrition

Contact Information for Business Card

Front of card : Logo ( on blue background )
Corinne Dalby
Nutrition & Fitness Coach for Seniors
Private gym at : 17 Fennick Street, Brantwood, Perth, WA 6291
Mob : 0412736158
Email : corinnedalby@fernpost.example
"For Seniors by a Senior"

Back of card
B.A. ( Soc.)
Dip. Ed. (Sec.)
Wellness Coach
Cert 4 Personal Trainer
Cert. Nutritition
MOVE ON Facilitator
Ageing Well Moving Freely Facilitator
NLP Master

```html
<!DOCTYPE html>
<html lang="en">
<head>
<meta charset="utf-8">
<title>Evergreen Vitality Studio – Business Card</title>
<link href="https://fonts.googleapis.com/css2?family=Open+Sans:wght@400;600;700&display=swap" rel="stylesheet">
<style>
  :root {
    --backdrop: #1b1b1b;
    --band: #6d6765;
    --frame: rgba(255,255,255,0.07);
    --card-blue: #0a72b6;
    --deep-blue: #0a3f61;
    --wave-light: rgba(61,155,224,0.35);
    --accent-yellow: #f3e21a;
    --text-white: #ffffff;
    --text-soft: #e6f1fa;
  }
  * { margin: 0; padding: 0; box-sizing: border-box; }
  html, body { width: 1200px; height: 900px; overflow: hidden; }
  body {
    background: var(--backdrop);
    font-family: "Open Sans", sans-serif;
    position: relative;
  }
  .band {
    position: absolute; left: 0; top: 320px; width: 1200px; height: 260px;
    background: var(--band);
  }
  .frame-outer {
    position: absolute; left: 25px; top: 85px; width: 1150px; height: 730px;
    border: 2px solid var(--frame); border-radius: 10px;
  }
  .frame-inner {
    position: absolute; left: 103px; top: 183px; width: 982px; height: 569px;
    border: 2px solid var(--frame);
  }
  .card {
    position: absolute;
    background: var(--card-blue);
    box-shadow: 3px 4px 6px rgba(0,0,0,0.6);
    overflow: hidden;
    color: var(--text-white);
  }
  .card-front { left: 127px; top: 92px; width: 595px; height: 332px; }
  .card-back { left: 469px; top: 470px; width: 596px; height: 330px; }

  .wave-area {
    position: absolute; left: 0; top: 0; width: 595px; height: 160px;
    background: linear-gradient(170deg, transparent 45%, var(--wave-light) 62%, transparent 80%);
  }

  .brand {
    position: absolute; left: 28px; top: 22px;
    display: flex; align-items: center; gap: 10px;
  }
  .brand-dot {
    width: 22px; height: 22px; border-radius: 50%;
    background: var(--accent-yellow);
  }
  .brand-name {
    font-size: 25px; font-weight: 600; color: var(--accent-yellow);
  }

  .holder-name {
    position: absolute; left: 26px; top: 182px;
    font-size: 25px; font-weight: 700; letter-spacing: 0.3px;
  }
  .holder-role {
    position: absolute; left: 112px; top: 211px;
    font-size: 11.5px; color: var(--text-soft);
  }

  .contact { position: absolute; left: 27px; top: 257px; list-style: none; }
  .contact li {
    display: flex; align-items: center; gap: 8px;
    font-size: 9.5px; color: var(--text-soft); height: 15px;
  }
  .contact li.phone { font-size: 11.5px; height: 16px; }
  .contact svg { width: 9px; height: 9px; flex: none; }

  .tagline {
    position: absolute; left: 407px; top: 277px; width: 188px; height: 22px;
    background: var(--deep-blue); border-radius: 4px 0 0 4px;
    font-size: 11px; display: flex; align-items: center; justify-content: center;
  }

  .symbol-area {
    position: absolute; left: 150px; top: 0; width: 446px; height: 330px;
    background: radial-gradient(ellipse at 62% 52%, rgba(10,63,97,0.75) 0%, rgba(10,63,97,0.35) 45%, transparent 72%);
  }

  .credentials { position: absolute; left: 50px; top: 84px; list-style: none; }
  .credentials li {
    font-size: 11.5px; color: var(--text-soft); height: 20.8px;
    display: flex; align-items: center; gap: 4px;
  }
  .credentials li::before {
    content: ""; width: 3px; height: 3px; border-radius: 50%;
    background: var(--accent-yellow);
  }
</style>
</head>
<body>
  <div class="band"></div>
  <div class="frame-outer"></div>
  <div class="frame-inner"></div>

  <section class="card card-front">
    <div class="wave-area" role="img" aria-label="Decorative light blue wave band sweeping across the top of the card"></div>

    <div class="brand">
      <span class="brand-dot"></span>
      <span class="brand-name">Evergreen Vitality Studio</span>
    </div>

    <h1 class="holder-name">Corinne Dalby</h1>
    <p class="holder-role">Nutrition &amp; Fitness Coach for Seniors</p>

    <ul class="contact">
      <li class="phone">
        <svg viewBox="0 0 10 10"><path d="M2 0.5 L3.6 2.6 L2.7 3.6 C3.3 5 4.8 6.6 6.3 7.3 L7.4 6.3 L9.5 8 L8.3 9.5 C4.5 9 1 5.5 0.5 1.7 Z" fill="var(--accent-yellow)"/></svg>
        0412-736-158
      </li>
      <li>
        <svg viewBox="0 0 10 10"><rect x="0.5" y="2" width="9" height="6.5" fill="var(--accent-yellow)"/><path d="M0.5 2 L5 5.8 L9.5 2" stroke="var(--card-blue)" stroke-width="0.9" fill="none"/></svg>
        corinnedalby@fernpost.example
      </li>
      <li>
        <svg viewBox="0 0 10 10"><path d="M5 0.5 C7.2 0.5 8.4 2.1 8.4 3.8 C8.4 6 5 9.5 5 9.5 C5 9.5 1.6 6 1.6 3.8 C1.6 2.1 2.8 0.5 5 0.5 Z" fill="var(--accent-yellow)"/><circle cx="5" cy="3.8" r="1.3" fill="var(--card-blue)"/></svg>
        Private gym at 17 Fennick Street, Brantwood, Perth, WA 6291
      </li>
    </ul>

    <p class="tagline">“For Seniors by a Senior”</p>
  </section>

  <section class="card card-back">
    <div class="symbol-area" role="img" aria-label="Large brand symbol decoration in deep blue and yellow"></div>
    <ul class="credentials">
      <li>B.A. (Soc.)</li>
      <li>Dip. Ed. (Sec.)</li>
      <li>Wellness Coach</li>
      <li>Cert 4 Personal Trainer</li>
      <li>Cert Nutrition</li>
      <li>MOVE ON Facilitator</li>
      <li>Ageing Well Moving Freely Facilitator</li>
      <li>NLP Master</li>
    </ul>
  </section>
</body>
</html>
```